IT Consulting Site Revamping for Varnel

I've put a skeleton together on my website, but realize I need some help (it's http://pilot.varnel-example.ca).
I've pulled together tidbits from other websites, but really need my site to be cleaned up, and really spruced up.
I primarily focus on the IT needs of small to medium size businesses, taking care of everything from their servers and networks down to their workstations.
I also want a page listing the vendors (and logos) that I work with including Brontisoft, QZWare, Pelvar, Fusk, TQ, ZRL, WUBE, Morva, Trelagate.
There should also be a simple form to get a quote that will email me.
The final design should communicate strength and reliability.
I would like this to be a fully functional website, that I can upload to Plimba Pages, with the same sort of pages that are existing on http://pilot.varnel-example.ca
Updates
Hey everyone,
Hi everyone,
Reason: Hi all,
There are some designers that would like to submit some new designs, so I'm extending the deadline.
Thanks,
Target Market(s)
Small to medium size business owners. This will primarily be males who work in the oil and gas industry.
Industry/Entity Type
Consulting
Look and feel
Each slider illustrates characteristics of the customer's brand and the style your logo design should communicate.

```html
<!DOCTYPE html>
<html lang="en">
<head>
<meta charset="utf-8">
<title>Varnel Solutions</title>
<link href="https://fonts.googleapis.com/css2?family=Nunito:wght@800&family=Open+Sans:ital,wght@0,300;0,400;0,700;1,700&family=Ubuntu:wght@400;500&display=swap" rel="stylesheet">
<style>
:root{
  --page:#f5f4f0;
  --blue:#1a8ed1;
  --blue-dark:#1272b0;
  --blue-light:#2fa9e6;
  --ink:#222;
  --grey:#6c6c6c;
  --rule:#9a9a9a;
  --footer:#2b2b2b;
  --footer-text:#d6d6d6;
  --tab:#3a3a3a;
}
*{margin:0;padding:0;box-sizing:border-box}
html,body{width:1108px;height:1200px;overflow:hidden;background:var(--page);font-family:"Open Sans",Arial,sans-serif;color:var(--ink)}
.canvas{position:relative;width:1108px;height:1200px}
.abs{position:absolute}

.brand{left:94px;top:22px;display:flex;align-items:center;gap:12px}
.brand-dot{width:76px;height:76px;border-radius:50%;background:var(--blue)}
.brand-name{font-family:"Ubuntu",sans-serif;font-weight:500;font-size:52px;color:var(--blue-dark);letter-spacing:-1px}

.phone{left:790px;top:6px;display:flex;align-items:center;gap:10px}
.phone-name{font-family:"Open Sans",sans-serif;font-weight:300;font-size:31px;color:#555;letter-spacing:2px}

.connect{left:712px;top:86px;display:flex;align-items:center;gap:8px;font-family:"Ubuntu",sans-serif;font-size:19px;color:#666}
.social{width:32px;height:32px;border-radius:50%;border:2px solid #fff;box-shadow:0 1px 2px rgba(0,0,0,.35)}
.s1{background:#3b5a9a}.s2{background:#3aa8dc}.s3{background:#e8731c}.s4{background:#d8d8d8}

.nav{left:0;top:132px;width:1108px;height:36px;background:linear-gradient(#34b0ea,#1583c6)}
.nav-home{left:102px;top:125px;width:88px;height:50px;background:linear-gradient(#4a4a4a,#1e1e1e);border-radius:4px;color:#fff;font-size:14px;display:flex;align-items:center;justify-content:center}
.nav-item{top:132px;height:36px;line-height:36px;color:#fff;font-size:14px}
.nav-sep{top:136px;width:1px;height:28px;background:rgba(0,0,0,.18);box-shadow:1px 0 0 rgba(255,255,255,.3)}

.slider{left:118px;top:199px;width:857px;height:317px;background:#fff;border-radius:10px;box-shadow:0 12px 14px -8px rgba(0,0,0,.35)}
.slide-photo{left:124px;top:205px;width:845px;height:305px;background:linear-gradient(90deg,#e8d3bd 0%,#f2ede7 35%,#eef1f4 55%,#b8c3cf 75%,#d7dadd 100%)}
.arrow{top:342px;width:47px;height:39px;background:linear-gradient(#444,#111);display:flex;align-items:center;justify-content:center}
.arrow-l{left:105px;border-radius:6px 20px 20px 6px}
.arrow-r{left:939px;border-radius:20px 6px 6px 20px}
.pager{left:506px;top:500px;width:102px;height:28px;background:#fff;border-radius:14px;border:1px solid #ddd;display:flex;align-items:center;justify-content:center;gap:3px}
.pager i{width:11px;height:11px;border-radius:50%;background:#8a8a8a}
.pager i.on{background:#fff;border:2px solid #8a8a8a}

.section-head{display:flex;align-items:center;gap:6px;font-family:"Ubuntu",sans-serif;color:#111}
.section-head .dot{border-radius:50%;background:var(--blue)}
.section-head b{font-weight:400;color:var(--blue)}
.about-head{left:108px;top:557px;font-size:25px}
.about-head .dot{width:52px;height:52px}
.about-rule{left:167px;top:605px;width:768px;border-top:1px dotted var(--rule)}
.about-copy{left:112px;top:625px;width:865px;font-size:10.6px;line-height:16.6px;color:#222}
.about-copy em{font-weight:700}
.about-copy p+p{margin-top:16.6px}

.more{display:flex;align-items:center;gap:4px;font-size:11px;color:#444}
.plus{width:21px;height:21px;border-radius:50%;background:radial-gradient(circle at 40% 35%,var(--blue-light),var(--blue-dark));position:relative}
.plus::before,.plus::after{content:"";position:absolute;background:#fff;left:50%;top:50%;transform:translate(-50%,-50%)}
.plus::before{width:11px;height:3px}.plus::after{width:3px;height:11px}

.services-head{left:112px;top:778px;font-size:23px}
.services-head .dot{width:30px;height:30px}
.grid{left:111px;top:822px;width:885px;height:233px;border-top:1px dotted var(--rule);border-left:1px dotted var(--rule);border-right:1px dotted var(--rule);display:flex}
.card{position:relative;flex:1;padding:11px 0 0 12px;border-right:1px dotted var(--rule);background:linear-gradient(90deg,transparent 85%,rgba(0,0,0,.05))}
.card:last-child{border-right:none}
.thumb{width:190px;height:102px;border:3px solid #fff;box-shadow:0 1px 3px rgba(0,0,0,.35)}
.t1{background:linear-gradient(90deg,#dfe3e8,#7b8592,#2e3d56)}
.t2{background:linear-gradient(120deg,#1b3fa8,#3a6fd6,#8c6d55)}
.t3{background:linear-gradient(150deg,#e9e9e9,#8f8f8f,#3d3d3d)}
.t4{background:linear-gradient(180deg,#3466c6,#0e1d3e)}
.card h3{font-family:"Nunito",sans-serif;font-weight:800;font-size:19px;color:#222;margin-top:10px;margin-left:3px}
.card h3 b{color:var(--blue)}
.card p{font-size:11px;line-height:16.6px;letter-spacing:.4px;color:#444;margin:4px 10px 0 3px;text-align:justify}
.card .more{position:absolute;right:4px;bottom:2px}

.footer{left:0;top:1080px;width:1108px;height:120px;background:var(--footer)}
.foot-brand{left:94px;top:1110px;display:flex;align-items:center;gap:12px}
.foot-brand .brand-dot{width:66px;height:66px;background:#8a8a8a}
.foot-brand .brand-name{font-size:44px;color:#9a9a9a}
.foot-links{left:352px;top:1122px;width:400px;text-align:center;font-size:11.5px;color:var(--footer-text);letter-spacing:.6px;line-height:19px}
.foot-links span{margin:0 12px}
.foot-contact{left:760px;top:1116px;width:242px;text-align:right;font-size:11.5px;color:var(--footer-text);letter-spacing:.8px;line-height:18.5px}
</style>
</head>
<body>
<div class="canvas">

  <div class="abs brand"><span class="brand-dot"></span><span class="brand-name">Varnel</span></div>

  <div class="abs phone">
    <svg width="36" height="36" viewBox="0 0 36 36"><circle cx="18" cy="18" r="18" fill="#1a8ed1"/><path d="M12 10c1-1 2.5-1 3 0l2 3c.5 1 0 2-1 2.5-1 .5 2 5 4 6 .6-1 1.6-1.4 2.5-1l3 2c1 .6 1 2 0 3-3 3-9 0-12-4s-4-9-1.5-11.5z" fill="#fff"/></svg>
    <span class="phone-name">08 5550 1400</span>
  </div>

  <div class="abs connect">Connect with us -:
    <span class="social s1"></span><span class="social s2"></span><span class="social s3"></span><span class="social s4"></span>
  </div>

  <nav>
    <div class="abs nav"></div>
    <div class="abs nav-home">Home</div>
    <div class="abs nav-sep" style="left:205px"></div>
    <div class="abs nav-item" style="left:228px">About us</div>
    <div class="abs nav-sep" style="left:322px"></div>
    <div class="abs nav-item" style="left:353px">Our Services</div>
    <div class="abs nav-sep" style="left:466px"></div>
    <div class="abs nav-item" style="left:492px">Our Products</div>
    <div class="abs nav-sep" style="left:611px"></div>
    <div class="abs nav-item" style="left:632px">Contact us</div>
  </nav>

  <div class="abs slider"></div>
  <div class="abs slide-photo" role="img" aria-label="Photo of a smiling support agent with a headset beside two businessmen reviewing a laptop"></div>
  <div class="abs arrow arrow-l"><svg width="14" height="16" viewBox="0 0 14 16"><path d="M3 2l7 6-7 6" stroke="#fff" stroke-width="3" fill="none"/></svg></div>
  <div class="abs arrow arrow-r"><svg width="14" height="16" viewBox="0 0 14 16"><path d="M11 2L4 8l7 6" stroke="#fff" stroke-width="3" fill="none"/></svg></div>
  <div class="abs pager"><i class="on"></i><i></i><i></i><i></i><i></i></div>

  <h2 class="abs section-head about-head"><span class="dot"></span>About <b>Company</b></h2>
  <div class="abs about-rule"></div>
  <div class="abs about-copy">
    <p><em><i>Lorem ipsum dolor sit amet, sit lectus blandit non nec egestas nulla, ac ut vitae massa blanditiis pulvinar, aenean enim nec sapien quis velit nunc, nunc fugiat velit purus ligula. In mattis curabitur id at aliquam, pede eu in massa nibh porttitor.</i></em> Tellus vestibulum nulla nunc nascetur nec, vestibulum ac malesuada velit tempus. Et iaculis ultricies, sapien sapien vitae odio, rutrum arcu. Vitae porttitor dapibus lacus id enim, in nulla, fermentum nec torquent ut erat habitasse.</p>
    <p>Cras felis enim, purus ut turpis, et lacus suspendisse, nullam a curabitur. Pede risus duis, et metus nisl metus pharetra. Et lacinia eget mauris morbi urna esse, pede pharsellus leo veniam ut justo. Id arcu cum semper tempus, eget lacus, phasellus conubia duis. Odio nibh hymenaeos laudantium at aptent, voluptate laoreet erat vel dignissim justo.</p>
  </div>
  <div class="abs more" style="left:904px;top:742px">View More <span class="plus"></span></div>

  <h2 class="abs section-head services-head"><span class="dot"></span>Our <b>Services</b></h2>
  <div class="abs grid">
    <div class="card">
      <div class="thumb t1" role="img" aria-label="Photo of a business team standing in a server room"></div>
      <h3><b>Managed</b> <b>IT</b> Services</h3>
      <p>Quis cum nibh tellus, dapibus est duis felis id proin molestie, duis tortor amet quam amet nec...</p>
      <div class="more">View More <span class="plus"></span></div>
    </div>
    <div class="card">
      <div class="thumb t2" role="img" aria-label="Photo of a technician working on network cables"></div>
      <h3><b>Networking</b> Services</h3>
      <p>Quis cum nibh tellus, dapibus est duis felis id proin molestie, duis tortor amet quam amet nec...</p>
      <div class="more">View More <span class="plus"></span></div>
    </div>
    <div class="card">
      <div class="thumb t3" role="img" aria-label="Photo of a USB flash drive close up"></div>
      <h3><b>Recovery</b> Backups</h3>
      <p>Quis cum nibh tellus, dapibus est duis felis id proin molestie, duis tortor amet quam amet nec...</p>
      <div class="more">View More <span class="plus"></span></div>
    </div>
    <div class="card">
      <div class="thumb t4" role="img" aria-label="Photo of a row of computer workstations"></div>
      <h3><b>Computer</b> Services</h3>
      <p>Quis cum nibh tellus, dapibus est duis felis id proin molestie, duis tortor amet quam amet nec...</p>
      <div class="more">View More <span class="plus"></span></div>
    </div>
  </div>

  <footer>
    <div class="abs footer"></div>
    <div class="abs foot-brand"><span class="brand-dot"></span><span class="brand-name">Varnel</span></div>
    <div class="abs foot-links">Home <span>|</span> About Us <span>|</span> Our Services <span>|</span> Our Products <span>|</span> Contact us<br>© 2012 Varnel Solutions, Inc. All rights reserved.</div>
    <div class="abs foot-contact">Telephone (02) 5550 1510<br>Facsimile (02) 5550 1620<br>Email info@varnelsolutions.example</div>
  </footer>

</div>
</body>
</html>
```